Havenry - "Where Pest Control is Free for Life..." Please see pitch deck...

Project goal, that this is a reusable template, not a one-off card
Brand and design direction, follow the logo, use the brand palette (with a color swatch table), typography and layout guidance
The Mark Vale placeholder content as a clean field-by-field table (name, title, company, address, office, cell, fax, email, havenry.com)
Print specs, 3.5 × 2 in trim, 0.125 in bleed, 300 DPI, CMYK, crop marks
Deliverables, layered editable PSD (your primary ask) plus vector .AI/.EPS and a press-ready PDF/X-1a, with fonts packaged
What you'll provide (logo, colors, fonts)
Process and sign-off, concept first, then full file package on approval.
Populate every field with this Mark Vale placeholder data so we can see the layout fully built out. We will replace it per person.
Name Mark Vale
Title Title / Position
Company Havenry
Address 487 Orchard Lane, Suite 210, Tallahassee, FL 32308
Office (850) 555-0142
Cell (850) 555-0167
Fax (850) 555-0181
Email markvale@havenry.com
Website havenry.com

We need the working, editable source files so we can update them ourselves, plus a ready-to-print export:
1. Photoshop (.PSD) — fully layered and editable, with each contact field on its own labeled text layer. This is the primary requested format.
2. Vector source — the press-standard editable format, Adobe Illustrator (.AI) and/or .EPS, since vector is preferred for crisp text and logos at print.
3. Print-ready PDF — press-quality (PDF/X-1a), CMYK, with bleed and crop marks, both sides.
4. Packaged fonts and links — include or list all fonts used, and package any linked assets so the files open correctly on our end.

Why both PSD and vector
The PSD covers our request directly and is easy for us to edit. Vector (.AI/.EPS) is what most commercial printers actually prefer for type and logos because it stays razor-sharp at any size. Providing both keeps us flexible no matter which printer we use. Have fun and keep it modern and cool the designer of the logo did a great job, see what you can do.

```html
<!DOCTYPE html>
<html lang="en">
<head>
<meta charset="utf-8">
<title>Havenry Business Card</title>
<link rel="stylesheet" href="https://fonts.googleapis.com/css2?family=Lato:wght@400;700;900&display=swap">
<style>
  :root {
    --page-bg: #e8e8e8;
    --card-white: #ffffff;
    --brand-navy: #0b1124;
    --brand-teal: #06b3c4;
    --text-gray: #555a60;
    --white: #ffffff;
  }
  * { margin: 0; padding: 0; box-sizing: border-box; }
  html, body {
    width: 1200px; height: 960px; overflow: hidden;
    background: var(--page-bg);
    font-family: "Lato", Arial, sans-serif;
  }
  .canvas { position: relative; width: 1200px; height: 960px; }

  /* Front side */
  .card-front {
    position: absolute; left: 124px; top: 78px;
    width: 703px; height: 402px;
    background: var(--card-white);
  }
  .wordmark {
    position: absolute; left: 36px; top: 40px;
    display: flex; align-items: center; gap: 10px;
    font-weight: 900; font-size: 64px; line-height: 1;
    color: var(--brand-navy); letter-spacing: -1px;
  }
  .wordmark-dot {
    width: 16px; height: 16px; background: var(--brand-teal); margin-top: 24px;
  }
  .person {
    position: absolute; left: 36px; top: 198px;
    display: flex; align-items: baseline; gap: 10px;
    line-height: 1;
  }
  .person-name { font-weight: 700; font-size: 33px; color: var(--brand-teal); }
  .person-company { font-weight: 400; font-size: 19.5px; color: var(--text-gray); }

  .contact-list {
    position: absolute; list-style: none;
    font-size: 19.5px; color: var(--text-gray); line-height: 23.2px;
  }
  .contact-list li { display: flex; align-items: center; gap: 11px; height: 23.2px; }
  .contact-list svg { width: 17px; height: 17px; flex: none; fill: var(--brand-teal); }
  .contact-phones { left: 36px; top: 254px; }
  .contact-online { left: 438px; top: 278px; }

  .address-band {
    position: absolute; left: 0; top: 342px; width: 703px; height: 33px;
    background: var(--brand-teal);
    display: flex; align-items: center; justify-content: center; gap: 8px;
    color: var(--white); font-size: 19.5px;
  }
  .address-band svg { width: 14px; height: 21px; fill: var(--white); }

  /* Back side */
  .card-back {
    position: absolute; left: 362px; top: 509px;
    width: 704px; height: 401px;
    background: var(--brand-navy);
    display: flex; align-items: center; justify-content: center;
  }
  .card-back-texture {
    position: absolute; inset: 0;
    background: radial-gradient(circle at 50% 50%, #0e1a2b 0%, var(--brand-navy) 75%);
  }
  .wordmark-reverse {
    position: relative; display: flex; align-items: center; gap: 12px;
    font-weight: 900; font-size: 76px; line-height: 1;
    color: var(--white); letter-spacing: -1px;
  }
  .wordmark-reverse .wordmark-dot { width: 19px; height: 19px; margin-top: 28px; }
</style>
</head>
<body>
<div class="canvas">

  <section class="card-front">
    <div class="wordmark">Havenry<span class="wordmark-dot"></span></div>

    <div class="person">
      <span class="person-name">Mark Vale</span>
      <span class="person-company">Company Havenry</span>
    </div>

    <ul class="contact-list contact-phones">
      <li>
        <svg viewBox="0 0 24 24" aria-hidden="true"><path d="M6.6 10.8a15 15 0 0 0 6.6 6.6l2.2-2.2a1 1 0 0 1 1-.25 11.4 11.4 0 0 0 3.6.57 1 1 0 0 1 1 1V20a1 1 0 0 1-1 1A17 17 0 0 1 3 4a1 1 0 0 1 1-1h3.5a1 1 0 0 1 1 1c0 1.25.2 2.45.57 3.6a1 1 0 0 1-.25 1z"/></svg>
        (850) 555-0142
      </li>
      <li>
        <svg viewBox="0 0 24 24" aria-hidden="true"><path d="M6 2h12a2 2 0 0 1 2 2v16a2 2 0 0 1-2 2H6a2 2 0 0 1-2-2V4a2 2 0 0 1 2-2zm1 3v13h10V5z"/></svg>
        (850) 555-0167
      </li>
      <li>
        <svg viewBox="0 0 24 24" aria-hidden="true"><path d="M6 2h12v6H6zM3 9h18v8h-3v-3H6v3H3zm4 6h10v7H7z"/></svg>
        (850) 555-0181
      </li>
    </ul>

    <ul class="contact-list contact-online">
      <li>
        <svg viewBox="0 0 24 24" aria-hidden="true"><path d="M12 2 2 9v12h20V9zm0 3 7 5-7 4-7-4z"/></svg>
        markvale@havenry.com
      </li>
      <li>
        <svg viewBox="0 0 24 24" aria-hidden="true"><path d="M12 2a10 10 0 1 0 0 20 10 10 0 0 0 0-20zm1 2.1c1.3.9 2.3 2.9 2.6 5.9H13zm-2 0V10H8.4c.3-3 1.3-5 2.6-5.9zM4.1 10h2.3c.1-2.2.6-4.1 1.4-5.4A8 8 0 0 0 4.1 10zm0 4a8 8 0 0 0 3.7 5.4c-.8-1.3-1.3-3.2-1.4-5.4zm4.3 0H11v5.9c-1.3-.9-2.3-2.9-2.6-5.9zm4.6 0h2.6c-.3 3-1.3 5-2.6 5.9zm4.6 0c-.1 2.2-.6 4.1-1.4 5.4a8 8 0 0 0 3.7-5.4zm2.3-4a8 8 0 0 0-3.7-5.4c.8 1.3 1.3 3.2 1.4 5.4z"/></svg>
        havenry.com
      </li>
    </ul>

    <div class="address-band">
      <svg viewBox="0 0 16 24" aria-hidden="true"><path d="M8 0a8 8 0 0 0-8 8c0 6 8 16 8 16s8-10 8-16a8 8 0 0 0-8-8zm0 11a3 3 0 1 1 0-6 3 3 0 0 1 0 6z"/></svg>
      487 Orchard Lane, Suite 210, Tallahassee, FL 32308
    </div>
  </section>

  <section class="card-back">
    <div class="card-back-texture" role="img" aria-label="Subtle repeating brand-mark pattern in dark navy tones"></div>
    <div class="wordmark-reverse">Havenry<span class="wordmark-dot"></span></div>
  </section>

</div>
</body>
</html>
```